Stationery for Public Accountant Practice

Name of Practice
Holloway Merrick Pty Ltd
Tel: 0413927056
Postal Address : PO Box 482, Oakvale East, Vic 3187

Target Market(s)

Small Business Clients

Industry/Entity Type

Accounting

Font styles to use
Serif

Requirements
Must have
• Letterhead, business card, With compliments slip
Nice to have
• Conservative

```html
<!DOCTYPE html>
<html lang="en">
<head>
<meta charset="utf-8">
<title>Holloway Merrick – Business Card</title>
<link rel="stylesheet" href="https://fonts.googleapis.com/css2?family=Cinzel:wght@400;500&family=Tinos:wght@400;700&display=swap">
<style>
  :root {
    --page-bg: #e9e9ea;
    --front-face: #5f5f61;
    --front-face-dark: #4a4a4c;
    --back-face: #ececec;
    --back-face-light: #f8f8f8;
    --band-dark: #141414;
    --band-mid: #6d6d6f;
    --band-light: #e6e6e6;
    --ink-light: #f1f1f1;
    --ink-dark: #3a3a3a;
    --ink-rule: #5a5a5a;
    --card-shadow: rgba(0, 0, 0, 0.28);
  }

  html, body {
    margin: 0;
    padding: 0;
    width: 1200px;
    height: 900px;
    overflow: hidden;
    background: var(--page-bg);
  }

  .canvas {
    width: 1200px;
    height: 900px;
    display: flex;
    flex-direction: column;
    align-items: center;
    justify-content: center;
    gap: 48px;
  }

  .business-card {
    position: relative;
    width: 640px;
    height: 366px;
    border-radius: 26px;
    overflow: hidden;
    box-shadow: 0 10px 28px var(--card-shadow);
  }

  .metal-band {
    position: absolute;
    left: 0;
    right: 0;
    height: 50px;
    background: linear-gradient(100deg,
      var(--band-dark) 0%,
      var(--band-mid) 22%,
      var(--band-dark) 38%,
      var(--band-light) 58%,
      var(--band-mid) 72%,
      var(--band-dark) 100%);
  }
  .metal-band--top { top: 0; }
  .metal-band--bottom { bottom: 0; }

  .card-face {
    position: absolute;
    top: 50px;
    bottom: 50px;
    left: 0;
    right: 0;
  }

  .business-card--front .card-face {
    background: linear-gradient(115deg, var(--front-face-dark) 0%, var(--front-face) 45%, #8a8a8c 55%, var(--front-face) 68%, var(--front-face-dark) 100%);
    display: flex;
    align-items: center;
    justify-content: center;
  }

  .business-card--back .card-face {
    background: linear-gradient(115deg, var(--back-face) 0%, var(--back-face-light) 50%, #d9d9d9 70%, var(--back-face) 100%);
  }

  .firm-name {
    font-family: "Cinzel", serif;
    font-weight: 400;
    letter-spacing: 1px;
    margin: 0;
    white-space: nowrap;
  }

  .business-card--front .firm-name {
    color: var(--ink-light);
    font-size: 44px;
  }

  .business-card--back .firm-name {
    position: absolute;
    top: 22px;
    left: 36px;
    color: var(--ink-dark);
    font-size: 40px;
  }

  .holder {
    position: absolute;
    top: 100px;
    left: 190px;
    width: 260px;
    text-align: center;
  }

  .holder-name {
    font-family: "Cinzel", serif;
    font-weight: 500;
    font-size: 21px;
    color: var(--ink-dark);
    letter-spacing: 1px;
    margin: 0;
  }

  .holder-rule {
    height: 1px;
    background: var(--ink-rule);
    margin: 4px 0 2px;
  }

  .holder-role {
    font-family: "Cinzel", serif;
    font-size: 12px;
    color: var(--ink-dark);
    letter-spacing: 4px;
    margin: 0;
  }

  .contact-block {
    position: absolute;
    bottom: 18px;
    left: 0;
    right: 0;
    text-align: center;
    font-family: "Tinos", serif;
    color: var(--ink-dark);
    font-size: 17px;
    line-height: 1.25;
  }

  .contact-block p { margin: 0; }
  .contact-company { font-weight: 700; }
</style>
</head>
<body>
  <main class="canvas">
    <section class="business-card business-card--front" aria-label="Business card front">
      <div class="metal-band metal-band--top"></div>
      <div class="card-face">
        <h1 class="firm-name">Holloway Merrick</h1>
      </div>
      <div class="metal-band metal-band--bottom"></div>
    </section>

    <section class="business-card business-card--back" aria-label="Business card back">
      <div class="metal-band metal-band--top"></div>
      <div class="card-face">
        <h2 class="firm-name">Holloway Merrick</h2>
        <div class="holder">
          <p class="holder-name">Daniel Ashby</p>
          <div class="holder-rule"></div>
          <p class="holder-role">Accountant</p>
        </div>
        <div class="contact-block">
          <p class="contact-company">Holloway Merrick Pty Ltd</p>
          <p>Telephone: 0413927056</p>
          <p>Postal Address : PO Box 482, Oakvale East, Vic 3187</p>
        </div>
      </div>
      <div class="metal-band metal-band--bottom"></div>
    </section>
  </main>
</body>
</html>
```